VANTA SWEEP

Need a professional looking business card that can fit : Name, Title, Cell, and office phone numbers. On the flip side we would like a list of our services : Highway accident management and towing, Crime scene clean up, Illegal drug lab clean up, Drug disposal, and Hazardous materials clean up.

```html
<!DOCTYPE html>
<html lang="en">
<head>
<meta charset="utf-8">
<title>Vanta Sweep Business Card</title>
<link rel="stylesheet" href="https://fonts.googleapis.com/css2?family=Ubuntu:wght@400;500;700&family=Roboto+Condensed:wght@400;700&display=swap">
<style>
  :root {
    --page: #f1f1f1;
    --card: #efefef;
    --navy: #263955;
    --gold: #c9aa1c;
    --red: #a8282a;
    --ink: #2a2f3a;
    --white: #ffffff;
  }
  * { margin: 0; padding: 0; box-sizing: border-box; }
  html, body {
    width: 1200px; height: 952px; overflow: hidden;
    background: var(--page);
    font-family: "Ubuntu", sans-serif;
  }
  .canvas { position: relative; width: 1200px; height: 952px; }
  .card {
    position: absolute; width: 560px; height: 320px;
    background: var(--card);
    box-shadow: 0 6px 18px rgba(0,0,0,0.12);
    overflow: hidden;
  }
  .card svg.waves { position: absolute; inset: 0; width: 100%; height: 100%; }
  .card--front { left: 560px; top: 110px; }
  .card--back { left: 80px; top: 500px; }

  .brand {
    position: absolute; display: flex; align-items: center; gap: 10px;
    font-family: "Ubuntu", sans-serif; font-weight: 700; color: var(--navy);
    letter-spacing: 0.04em;
  }
  .brand__dot { border-radius: 50%; background: var(--navy); flex: none; }
  .card--front .brand { left: 36px; top: 48px; font-size: 24px; }
  .card--front .brand__dot { width: 22px; height: 22px; }

  .address {
    position: absolute; left: 40px; top: 136px;
    font-family: "Roboto Condensed", sans-serif; font-size: 14px; color: var(--ink);
  }
  .person { position: absolute; right: 34px; top: 78px; text-align: right; }
  .person__name {
    font-family: "Ubuntu", sans-serif; font-weight: 700; font-size: 22px; color: var(--red);
  }
  .person__title {
    font-family: "Roboto Condensed", sans-serif; font-size: 15px; color: var(--ink); margin-top: 2px;
  }
  .contact {
    position: absolute; right: 30px; bottom: 30px; list-style: none;
    font-family: "Roboto Condensed", sans-serif; font-size: 13px; color: var(--white);
  }
  .contact li { display: flex; align-items: center; justify-content: flex-end; gap: 8px; line-height: 22px; }
  .contact svg { width: 13px; height: 13px; fill: var(--white); }

  .services { position: absolute; left: 48px; top: 26px; }
  .services__heading {
    font-weight: 700; font-size: 21px; color: var(--red); margin-bottom: 4px;
  }
  .services__list { list-style: none; font-size: 17px; color: var(--navy); line-height: 24px; }
  .services__list li::before { content: "»"; margin-right: 14px; font-size: 14px; }
  .card--back .brand {
    right: 34px; bottom: 40px; font-size: 18px; color: var(--gold);
  }
  .card--back .brand__dot { width: 16px; height: 16px; background: var(--gold); }
</style>
</head>
<body>
<main class="canvas">

  <section class="card card--front" aria-label="Business card front">
    <svg class="waves" viewBox="0 0 560 320" preserveAspectRatio="none" aria-hidden="true">
      <path d="M0 175 C120 230 230 240 330 218 C430 196 500 190 560 196 L560 320 L0 320 Z" fill="var(--navy)"/>
      <path d="M0 190 C100 235 210 250 330 226 C430 206 500 200 560 200 L560 320 L0 320 Z" fill="var(--card)"/>
      <path d="M0 168 C110 235 220 250 330 232 C440 214 500 208 560 206 L560 320 L0 320 Z" fill="var(--gold)"/>
      <path d="M0 176 C110 245 220 258 330 240 C440 222 500 214 560 212 L560 320 L0 320 Z" fill="var(--card)"/>
      <path d="M0 205 C120 262 230 272 330 252 C430 232 500 222 560 220 L560 320 L0 320 Z" fill="var(--navy)"/>
    </svg>
    <div class="brand"><span class="brand__dot"></span>VANTA SWEEP</div>
    <p class="address">Your office address</p>
    <div class="person">
      <p class="person__name">Your Name</p>
      <p class="person__title">Title</p>
    </div>
    <ul class="contact">
      <li>00.00.00.0000
        <svg viewBox="0 0 24 24"><path d="M12 2a7 7 0 0 0-7 7c0 5 7 13 7 13s7-8 7-13a7 7 0 0 0-7-7zm0 9.5A2.5 2.5 0 1 1 12 6.5a2.5 2.5 0 0 1 0 5z"/></svg></li>
      <li>yourname@yourwebsite.com
        <svg viewBox="0 0 24 24"><path d="M2 5h20v14H2z M3 6l9 7 9-7" fill="none" stroke="#fff" stroke-width="2"/></svg></li>
      <li>www.yourwebsite.com
        <svg viewBox="0 0 24 24"><circle cx="12" cy="12" r="9" fill="none" stroke="#fff" stroke-width="2"/><path d="M3 12h18M12 3c3 3 3 15 0 18M12 3c-3 3-3 15 0 18" fill="none" stroke="#fff" stroke-width="1.6"/></svg></li>
    </ul>
  </section>

  <section class="card card--back" aria-label="Business card back">
    <svg class="waves" viewBox="0 0 560 320" preserveAspectRatio="none" aria-hidden="true">
      <path d="M0 150 C100 215 200 240 310 232 C420 224 500 226 560 232 L560 320 L0 320 Z" fill="var(--gold)"/>
      <path d="M0 162 C100 228 200 250 310 242 C420 234 500 234 560 238 L560 320 L0 320 Z" fill="var(--card)"/>
      <path d="M0 196 C100 246 200 262 310 252 C420 242 500 242 560 244 L560 320 L0 320 Z" fill="var(--navy)"/>
    </svg>
    <div class="services">
      <h2 class="services__heading">Our Services :</h2>
      <ul class="services__list">
        <li>Highway accident management and towing</li>
        <li>Crime scene clean up</li>
        <li>Illegal drug lab clean up</li>
        <li>Drug disposal</li>
        <li>Hazardous materials clean up</li>
      </ul>
    </div>
    <div class="brand"><span class="brand__dot"></span>VANTA SWEEP</div>
  </section>

</main>
</body>
</html>
```